Social Media Infographic for White Paper

Am working on a white paper on social media use by C-Suite Executives, and hope to include some infographics. I would like some help designing the first infographic.

The master bit of information is that "66% of C-Suite Executives use social media for professional purpose."

Within that 66%
-70% post original content on a daily/weekly basis
-13% of professional users are lurkers
-40% plan to use social media even more in the future

After initial design will need to two versions of the infographic, one listing the source at the bottom in small print (Source: 2017 Thornwick Partners Executive Social Media Study), the other one with no source information.

Infographic design should be complimentary with my website: www.thornwickpartners.example, but use of green should be very limited, if at all.

Target Market(s)

New media, C-Suite Executives, Executive Coaches

Industry/Entity Type

Management Consulting

Font styles to use
Sans Serif

Requirements
Must have
• Infographic with data displayed in a easy to understand format that tells the story of C-Suite Executives that participate in social media for professional purposes.
Nice to have
• Complements website design - www.thornwick.example.
Should not have
• Limit use of green from website logo, which can be overpowering. Some is ok, but not too much

```html
<!DOCTYPE html>
<html lang="en">
<head>
<meta charset="utf-8">
<title>C-Suite Executives on Social Media – Thornwick Partners</title>
<link rel="stylesheet" href="https://fonts.googleapis.com/css2?family=Montserrat:wght@800&family=Open+Sans:wght@400;600;700&family=Oswald:wght@300;400&display=swap">
<style>
  :root {
    --page: #ffffff;
    --band-light: #f1eff0;
    --band-footer: #eeeeee;
    --panel-dark: #363435;
    --map-tone: #444244;
    --green: #6a9e35;
    --green-bright: #8cc43f;
    --salmon: #e8725f;
    --crimson: #c8304e;
    --blue: #0b7bb5;
    --ring-gray: #d7d9da;
    --ink: #262626;
    --bubble-blue: #b3d5f2;
    --bubble-green: #a8d65a;
    --white: #ffffff;
  }
  * { margin: 0; padding: 0; box-sizing: border-box; }
  html, body { width: 1200px; height: 1000px; overflow: hidden; background: var(--page); }
  .infographic { position: relative; width: 1200px; height: 1000px; font-family: "Open Sans", Arial, sans-serif; }

  .headline-band { position: absolute; left: 145px; top: 28px; width: 910px; height: 226px; background: var(--band-light); }
  .headline-arrow { position: absolute; left: 0; top: 0; }
  .headline-figure { position: absolute; left: 26px; top: 62px; font-family: "Montserrat", Arial, sans-serif; font-weight: 800; font-size: 94px; line-height: 1; color: var(--white); letter-spacing: 1px; white-space: nowrap; }
  .headline-title { position: absolute; left: 278px; top: 44px; font-family: "Montserrat", Arial, sans-serif; font-weight: 800; font-size: 49px; line-height: 1; color: var(--ink); letter-spacing: 1.5px; white-space: nowrap; }
  .headline-sub { position: absolute; left: 283px; top: 116px; font-size: 30px; line-height: 38px; color: var(--green); letter-spacing: 1px; white-space: nowrap; }
  .chat-bubbles { position: absolute; left: 740px; top: 95px; }

  .stats-panel { position: absolute; left: 145px; top: 254px; width: 910px; height: 587px; background: var(--panel-dark); overflow: hidden; }
  .world-map { position: absolute; left: 90px; top: 140px; width: 820px; height: 420px; border-radius: 40px; background: radial-gradient(ellipse at 50% 40%, var(--map-tone), rgba(68,66,68,0) 75%); }
  .section-tag { position: absolute; left: 0; top: 33px; width: 372px; height: 78px; background: var(--salmon); color: var(--white); font-family: "Oswald", "Arial Narrow", sans-serif; font-weight: 300; font-size: 56px; line-height: 78px; padding-left: 28px; white-space: nowrap; overflow: hidden; }
  .section-tag span { display: inline-block; transform: scaleX(0.86); transform-origin: left center; }
  .donuts { position: absolute; left: 0; top: 0; }
  .stat-value { font-family: "Open Sans", Arial, sans-serif; font-weight: 700; font-size: 50px; fill: var(--white); }
  .stat-label { position: absolute; top: 466px; height: 60px; color: var(--white); font-size: 19px; line-height: 25px; white-space: nowrap; }
  .stat-label svg { position: absolute; left: 0; top: 0; }
  .stat-label span { position: relative; display: block; padding-top: 5px; }
  .label-content { left: 35px; width: 247px; }
  .label-content span { padding-left: 8px; }
  .label-lurkers { left: 331px; width: 245px; text-align: center; }
  .label-future { left: 623px; width: 246px; }
  .label-future span { padding-left: 14px; }

  .footer-band { position: absolute; left: 145px; top: 841px; width: 910px; height: 130px; background: var(--band-footer); }
  .brand { position: absolute; left: 34px; top: 24px; display: flex; align-items: center; gap: 12px; }
  .brand-mark { width: 62px; height: 62px; border-radius: 50%; background: var(--green); }
  .brand-name { font-family: "Open Sans", Arial, sans-serif; font-weight: 700; font-size: 27px; color: var(--green); white-space: nowrap; }
  .brand-url { position: absolute; left: 40px; top: 98px; font-size: 15px; color: var(--ink); white-space: nowrap; }
  .source { position: absolute; right: 32px; top: 43px; text-align: right; font-size: 15px; line-height: 19px; color: var(--ink); white-space: nowrap; }
  .source-heading { padding-right: 8px; }
</style>
</head>
<body>
<main class="infographic">

  <header class="headline-band">
    <svg class="headline-arrow" width="270" height="226" viewBox="0 0 270 226" aria-hidden="true">
      <polygon points="0,0 225,0 268,113 225,226 0,226" fill="var(--green)"/>
    </svg>
    <div class="headline-figure">66%</div>
    <h1 class="headline-title">of C-Suite Executives</h1>
    <p class="headline-sub">USE SOCIAL MEDIA<br>FOR PROFESSIONAL PURPOSE</p>
    <svg class="chat-bubbles" width="160" height="125" viewBox="0 0 160 125" aria-hidden="true">
      <ellipse cx="103" cy="70" rx="45" ry="39" fill="var(--bubble-green)"/>
      <polygon points="120,100 135,122 108,104" fill="var(--bubble-green)"/>
      <ellipse cx="49" cy="45" rx="47" ry="40" fill="var(--bubble-blue)"/>
      <polygon points="28,75 18,100 45,82" fill="var(--bubble-blue)"/>
      <circle cx="31" cy="45" r="6" fill="var(--white)"/>
      <circle cx="49" cy="45" r="6" fill="var(--white)"/>
      <circle cx="67" cy="45" r="6" fill="var(--white)"/>
    </svg>
  </header>

  <section class="stats-panel">
    <div class="world-map" role="img" aria-label="Faint world map with dotted connection lines and small network icons"></div>
    <h2 class="section-tag"><span>Within that 66%</span></h2>

    <svg class="donuts" width="910" height="587" viewBox="0 0 910 587">
      <g transform="translate(170,329)">
        <circle r="86" fill="none" stroke="var(--ring-gray)" stroke-width="22"/>
        <circle r="86" fill="none" stroke="var(--green-bright)" stroke-width="22" stroke-dasharray="378.2 540.4" transform="rotate(-90) scale(1,-1)"/>
        <text class="stat-value" text-anchor="middle" y="18">70%</text>
      </g>
      <g transform="translate(452,329)">
        <circle r="86" fill="none" stroke="var(--ring-gray)" stroke-width="22"/>
        <circle r="86" fill="none" stroke="var(--crimson)" stroke-width="22" stroke-dasharray="70.3 540.4" transform="rotate(-90) scale(1,-1)"/>
        <text class="stat-value" text-anchor="middle" y="18">13%</text>
      </g>
      <g transform="translate(735,329)">
        <circle r="86" fill="none" stroke="var(--ring-gray)" stroke-width="22"/>
        <circle r="86" fill="none" stroke="var(--blue)" stroke-width="22" stroke-dasharray="216.2 540.4" transform="rotate(-90) scale(1,-1)"/>
        <text class="stat-value" text-anchor="middle" y="18">40%</text>
      </g>
    </svg>

    <div class="stat-label label-content">
      <svg width="247" height="60" aria-hidden="true"><polygon points="0,0 247,0 226,60 0,60" fill="var(--green-bright)"/></svg>
      <span>post original content<br>on a daily/weekly basis</span>
    </div>
    <div class="stat-label label-lurkers">
      <svg width="245" height="60" aria-hidden="true"><rect width="245" height="60" fill="var(--crimson)"/></svg>
      <span>of professional users<br>are lurkers</span>
    </div>
    <div class="stat-label label-future">
      <svg width="246" height="60" aria-hidden="true"><polygon points="18,0 246,0 246,60 0,60" fill="var(--blue)"/></svg>
      <span>plan to use social media<br>&nbsp;&nbsp;even more in the future</span>
    </div>
  </section>

  <footer class="footer-band">
    <div class="brand">
      <div class="brand-mark"></div>
      <div class="brand-name">Thornwick Partners</div>
    </div>
    <div class="brand-url">www.thornwickpartners.example</div>
    <div class="source">
      <div class="source-heading">Source:</div>
      <div>2017 Thornwick Partners Executive</div>
      <div>Social Media Study</div>
    </div>
  </footer>

</main>
</body>
</html>
```